Poster Design Project - Front Window Poster for IT Business

Design a poster to be displayed in the front window of our office.
To include the following text:
Proactive Network Solutions
Servers & Networks
Workly 480
Cloud Solutions
Helpdesk Services & Support
Network Audits
Disaster Recovery
IT Consulting
Contact details to be shown on the poster:
www.qe.com.au
02 5550 1824
Please also include the logo and related colour scheme.
Needs to look professional and easy to read from the street.
Must be in A1 format, printable through quillomark.
Hi Designers,
Nadia

```html
<!DOCTYPE html>
<html lang="en">
<head>
<meta charset="utf-8">
<title>QE Technology Solutions – Proactive Network Solutions</title>
<link rel="stylesheet" href="https://fonts.googleapis.com/css2?family=Source+Sans+3:wght@400;600;700&display=swap">
<style>
  :root {
    --blue-deep: #1b5fb8;
    --blue-mid: #2b86d8;
    --blue-soft: #8cc3ee;
    --blue-pale: #dcecf9;
    --headline: #2a86d6;
    --ink: #1e1e1e;
    --white: #ffffff;
    --photo-frame: #ffffff;
  }
  * { box-sizing: border-box; margin: 0; padding: 0; }
  html, body { width: 854px; height: 1200px; overflow: hidden; background: var(--white); }
  body { font-family: "Source Sans 3", "Myriad Pro", Arial, sans-serif; }

  .poster { position: relative; width: 854px; height: 1200px; overflow: hidden; background: var(--white); }

  .band { position: absolute; left: 0; width: 854px; }
  .band-top {
    top: 0; height: 300px;
    background: linear-gradient(to bottom, #3f8fe0 0%, #8cc3ee 45%, #dcecf9 78%, #ffffff 100%);
  }
  .band-lower {
    top: 760px; height: 180px;
    background: linear-gradient(to bottom, rgba(255,255,255,0) 0%, #bcdcf5 40%, #5aa4e6 80%, #2b86d8 100%);
  }
  .band-footer { top: 940px; height: 260px; background: var(--blue-mid); }

  .brand-top {
    position: absolute; left: 0; right: 0; top: 58px;
    text-align: center; color: var(--blue-deep); font-weight: 700;
  }
  .brand-top .brand-initials { display: block; font-size: 180px; line-height: 150px; letter-spacing: 2px; }
  .brand-top .brand-descriptor { display: block; font-size: 31px; line-height: 36px; letter-spacing: 2px; margin-top: 6px; }

  .headline {
    position: absolute; left: 68px; top: 304px;
    font-size: 62px; line-height: 70px; font-weight: 400; color: var(--headline); white-space: nowrap;
  }

  .services { position: absolute; left: 68px; top: 405px; list-style: none; }
  .services li { font-size: 35px; line-height: 52px; color: var(--ink); white-space: nowrap; }

  .photo {
    position: absolute; border-radius: 50%;
    border: 4px solid var(--photo-frame);
    box-shadow: 0 4px 10px rgba(0, 40, 90, 0.35);
  }
  .photo-monitor { left: 540px; top: 416px; width: 158px; height: 158px;
    background: radial-gradient(circle at 40% 35%, #e9f3fa, #8fb6d3 70%, #4d7696); }
  .photo-padlock { left: 669px; top: 578px; width: 136px; height: 136px;
    background: radial-gradient(circle at 45% 40%, #f6dc7c, #c8962a 65%, #7a5410); }
  .photo-cable { left: 540px; top: 668px; width: 116px; height: 116px;
    background: radial-gradient(circle at 50% 50%, #c9b6ee, #6c4fb4 60%, #2a1a58); }
  .photo-keyboard { left: 597px; top: 794px; width: 150px; height: 150px;
    background: radial-gradient(circle at 50% 40%, #e8e8e8, #9a9a9a 65%, #4e4e4e); }

  .brand-bottom {
    position: absolute; left: 51px; top: 1058px; color: var(--white); font-weight: 700;
  }
  .brand-bottom .brand-initials { display: block; font-size: 100px; line-height: 88px; letter-spacing: 1px; }
  .brand-bottom .brand-descriptor { display: block; font-size: 17.5px; line-height: 20px; letter-spacing: 1px; margin-top: 2px; }

  .contact { position: absolute; right: 34px; top: 1056px; text-align: right; color: var(--white); }
  .contact .call { font-size: 37px; line-height: 46px; font-weight: 400; white-space: nowrap; }
  .contact .call .phone { margin-left: 28px; }
  .contact .web { font-size: 37px; line-height: 50px; white-space: nowrap; }
</style>
</head>
<body>
<main class="poster">
  <div class="band band-top" aria-hidden="true"></div>
  <div class="band band-lower" aria-hidden="true"></div>
  <div class="band band-footer" aria-hidden="true"></div>

  <header class="brand-top" aria-label="QE Technology Solutions">
    <span class="brand-initials">QE</span>
    <span class="brand-descriptor">TECHNOLOGY SOLUTIONS</span>
  </header>

  <h1 class="headline">Proactive Network Solutions</h1>

  <ul class="services">
    <li>Servers &amp; Networks</li>
    <li>Workly 480</li>
    <li>Cloud Solutions</li>
    <li>Helpdesk Services &amp; Support</li>
    <li>Network Audits</li>
    <li>Disaster Recovery</li>
    <li>IT Consulting</li>
  </ul>

  <div class="photo photo-monitor" role="img" aria-label="Close-up photo of a computer monitor stand on a desk"></div>
  <div class="photo photo-padlock" role="img" aria-label="Photo of a gold padlock on a chain"></div>
  <div class="photo photo-cable" role="img" aria-label="Photo of a network cable connector in purple light"></div>
  <div class="photo photo-keyboard" role="img" aria-label="Black and white photo of hands typing on a keyboard"></div>

  <footer>
    <div class="brand-bottom" aria-label="QE Technology Solutions">
      <span class="brand-initials">QE</span>
      <span class="brand-descriptor">TECHNOLOGY SOLUTIONS</span>
    </div>
    <div class="contact">
      <p class="call">CALL US NOW -<span class="phone">02 5550 1824</span></p>
      <p class="web">www.qe.com.au</p>
    </div>
  </footer>
</main>
</body>
</html>
```